Business card revamp

we are refrigeration mechanic i need a modern professional double side business card using my current branding
The card information must have site address~ 17 Pellham st Tarrowell, Vic 3718 postal address~ P.o. Box 862 Tarrowell,Vic 3719 Phone Number~0358941637 Fax Nunber~0358936205 Email address~ brettk@vorlatek.com.au Title~ Manager Licence numbers~ AU47319, NSW 481927D Web site~ www.frostwaylane.com.au

```html
<!DOCTYPE html>
<html lang="en">
<head>
<meta charset="utf-8">
<title>Frostway Lane – Business Card</title>
<link href="https://fonts.googleapis.com/css2?family=Roboto+Condensed:wght@400;700&display=swap" rel="stylesheet">
<style>
  :root {
    --canvas: #dcdcdc;
    --paper: #ffffff;
    --brand-blue: #1a62b8;
    --deep-blue: #0f56a5;
    --ink-light: #ffffff;
  }
  html, body {
    margin: 0;
    width: 1200px;
    height: 1011px;
    overflow: hidden;
    background: var(--canvas);
    font-family: "Roboto Condensed", Arial, sans-serif;
  }
  .stage {
    position: relative;
    width: 1200px;
    height: 1011px;
  }
  .card {
    position: absolute;
    top: 200px;
    width: 370px;
    height: 605px;
    background: var(--paper);
    overflow: hidden;
    box-shadow: 0 6px 18px rgba(0,0,0,0.18);
  }
  .card--front { left: 185px; }
  .card--back { left: 645px; }

  .front-shape { position: absolute; inset: 0; }

  .brand-name {
    color: var(--brand-blue);
    font-weight: 700;
    font-size: 34px;
    letter-spacing: 1px;
    text-transform: uppercase;
    margin: 0;
    white-space: nowrap;
  }
  .front-brand {
    position: absolute;
    top: 62px;
    left: 0;
    width: 100%;
    text-align: center;
  }
  .licence {
    position: absolute;
    top: 146px;
    left: 0;
    width: 100%;
    margin: 0;
    text-align: center;
    color: var(--brand-blue);
    font-size: 20px;
    line-height: 1.25;
  }
  .licence__label { font-weight: 700; display: block; }

  .contact-block {
    position: absolute;
    top: 335px;
    left: 48px;
    right: 20px;
    color: var(--ink-light);
  }
  .person-name { font-weight: 700; font-size: 23px; margin: 0; }
  .person-title { font-size: 19px; margin: 2px 0 22px; }
  .contact-list { list-style: none; margin: 0; padding: 0; font-size: 18px; }
  .contact-list li {
    display: flex;
    align-items: flex-start;
    gap: 12px;
    margin-bottom: 8px;
    line-height: 1.2;
    white-space: nowrap;
  }
  .contact-list svg { flex: 0 0 16px; width: 16px; height: 16px; margin-top: 2px; }

  .back-ring {
    position: absolute;
    top: 172px;
    left: 55px;
    width: 256px;
    height: 256px;
    border: 3px solid var(--deep-blue);
    border-radius: 50%;
    display: flex;
    align-items: center;
    justify-content: center;
  }
  .back-ring .brand-name { font-size: 30px; }
</style>
</head>
<body>
<main class="stage">

  <section class="card card--front" aria-label="Business card front">
    <svg class="front-shape" viewBox="0 0 370 605" aria-hidden="true">
      <path d="M0 250 Q185 315 370 185 L370 605 L0 605 Z" fill="var(--brand-blue)"/>
      <path d="M0 236 Q185 301 370 171" fill="none" stroke="var(--brand-blue)" stroke-width="4"/>
    </svg>

    <div class="front-brand"><p class="brand-name">Frostway Lane</p></div>
    <p class="licence">
      <span class="licence__label">Licence Numbers:</span>
      AU47319 | NSW 481927D
    </p>

    <div class="contact-block">
      <p class="person-name">Brett Kalinowski</p>
      <p class="person-title">Manager</p>
      <ul class="contact-list">
        <li>
          <svg viewBox="0 0 16 16" aria-hidden="true"><path d="M8 1a5 5 0 0 0-5 5c0 4 5 9 5 9s5-5 5-9a5 5 0 0 0-5-5zm0 7a2 2 0 1 1 0-4 2 2 0 0 1 0 4z" fill="#fff"/></svg>
          <span>17 Pellham st Tarrowell, Vic 3718<br>P.o. Box 862 Tarrowell,Vic 3719</span>
        </li>
        <li>
          <svg viewBox="0 0 16 16" aria-hidden="true"><circle cx="8" cy="8" r="7.5" fill="#fff"/><path d="M5.5 4l1.5 2-1 1c.6 1.3 1.7 2.4 3 3l1-1 2 1.5-1 1.5C8 12 4 8 4 5z" fill="var(--brand-blue)"/></svg>
          <span>0358941637</span>
        </li>
        <li>
          <svg viewBox="0 0 16 16" aria-hidden="true"><circle cx="8" cy="8" r="7.5" fill="#fff"/><rect x="4" y="6" width="8" height="5" fill="var(--brand-blue)"/><rect x="5.5" y="3.5" width="5" height="3" fill="var(--brand-blue)"/></svg>
          <span>0358936205</span>
        </li>
        <li>
          <svg viewBox="0 0 16 16" aria-hidden="true"><circle cx="8" cy="8" r="7.5" fill="#fff"/><rect x="4" y="5" width="8" height="6" fill="none" stroke="var(--brand-blue)" stroke-width="1.2"/><path d="M4 5l4 3.5L12 5" fill="none" stroke="var(--brand-blue)" stroke-width="1.2"/></svg>
          <span>brettk@vorlatek.com.au</span>
        </li>
        <li>
          <svg viewBox="0 0 16 16" aria-hidden="true"><g fill="none" stroke="#fff" stroke-width="1.2"><circle cx="8" cy="8" r="7"/><ellipse cx="8" cy="8" rx="3" ry="7"/><path d="M1 8h14M2.5 4.5h11M2.5 11.5h11"/></g></svg>
          <span>www.frostwaylane.com.au</span>
        </li>
      </ul>
    </div>
  </section>

  <section class="card card--back" aria-label="Business card back">
    <div class="back-ring"><p class="brand-name">Frostway Lane</p></div>
  </section>

</main>
</body>
</html>
```